ORVILMA card Technical Architecture

Hello everyone ORVILMA: It is a consulting firm in Architecture and Construction. I require a card duplexing, sober, elegant, classic but not boring. Update 1: Use the following data for the card. Name: Rodrigo Salinas Tomás Quevedo Position: COO Twitter: @orvilmaAT Homepage: orvilma.com home address not include the participation of all thank you.

Target Market(s)

Construction companies, Architects and Consulting Engineers

Industry/Entity Type

Consulting

Contact Information for Business Card

Los campos que debe tener:
Nombre, Cargo, email, homepage y twitter

Font styles to use
Serif
Sans Serif
Other font styles liked:
• Me gustan playfair display, open sans y roboto, pero estoy sujeto a sus propuestas

Requirements
Must have
• Colors: Present combined proposals in white, red, gray and black Update 1: The two names must be clearly differentiated from the two surnames
Nice to have
• They are free to present their best proposals. I will bring them immediate feedback to the extent you can go see their designs. Complete data for card and logo files will give the winner the

```html
<!DOCTYPE html>
<html lang="es">
<head>
<meta charset="utf-8">
<title>ORVILMA – Business Card</title>
<link rel="stylesheet" href="https://fonts.googleapis.com/css2?family=Open+Sans:wght@400;600;700&display=swap">
<style>
  :root {
    --stage-top: #262626;
    --stage-bottom: #050505;
    --card-white: #ffffff;
    --brand-red: #d11f2e;
    --red-core: #c41f26;
    --red-edge: #7c0509;
    --ink: #333333;
    --on-red: #ffffff;
  }
  * { margin: 0; padding: 0; box-sizing: border-box; }
  html, body { width: 1200px; height: 900px; overflow: hidden; }
  body {
    position: relative;
    font-family: "Open Sans", sans-serif;
    background: linear-gradient(180deg, var(--stage-top) 0%, #141414 55%, var(--stage-bottom) 100%);
  }
  .card {
    position: absolute;
    top: 306px;
    width: 440px;
    height: 271px;
    border-radius: 12px;
    overflow: hidden;
  }
  .card--front { left: 149px; background: var(--card-white); }
  .card--back {
    left: 608px;
    background: radial-gradient(ellipse 60% 70% at 50% 42%, var(--red-core) 0%, #a8131a 55%, var(--red-edge) 100%);
    color: var(--on-red);
    text-align: center;
  }

  /* Front */
  .front-brand {
    position: absolute;
    left: 50px;
    top: 120px;
    width: 150px;
    font-size: 20px;
    font-weight: 700;
    letter-spacing: 2px;
    color: var(--brand-red);
  }
  .contact { position: absolute; left: 230px; top: 78px; }
  .contact__name { font-size: 14.5px; font-weight: 600; color: var(--brand-red); line-height: 18px; }
  .contact__role { font-size: 12px; color: var(--ink); line-height: 15px; }
  .contact__list { list-style: none; margin-top: 20px; }
  .contact__item {
    display: flex; align-items: center; gap: 8px;
    font-size: 12px; line-height: 16px; color: var(--ink);
  }
  .contact__icon { width: 8px; height: 8px; flex: none; }

  /* Back */
  .back-mark {
    display: block;
    margin: 62px auto 0;
    width: 64px; height: 64px;
    border: 3px solid var(--on-red);
    border-radius: 50%;
  }
  .wordmark {
    margin-top: 18px;
    font-size: 38px;
    font-weight: 400;
    letter-spacing: 13px;
    padding-left: 13px;
    line-height: 42px;
  }
  .rule {
    width: 307px; height: 1px; margin: 6px auto 0;
    background: rgba(255,255,255,0.75);
  }
  .tagline {
    margin-top: 4px;
    font-size: 13.5px;
    letter-spacing: 3.4px;
    padding-left: 3px;
  }
</style>
</head>
<body>
  <section class="card card--front" aria-label="Card front">
    <div class="front-brand">ORVILMA</div>
    <div class="contact">
      <p class="contact__name">Daniel Moreno</p>
      <p class="contact__role">Managing Director</p>
      <ul class="contact__list">
        <li class="contact__item">
          <svg class="contact__icon" viewBox="0 0 8 8" aria-hidden="true"><rect x="1.5" y="0" width="5" height="8" rx="1" fill="var(--brand-red)"/><rect x="2.5" y="1" width="3" height="5" fill="#fff"/></svg>
          123 456 789
        </li>
        <li class="contact__item">
          <svg class="contact__icon" viewBox="0 0 8 8" aria-hidden="true"><rect x="0" y="1.5" width="8" height="5" fill="var(--brand-red)"/><path d="M0 1.5 L4 4.5 L8 1.5" stroke="#fff" stroke-width="0.8" fill="none"/></svg>
          info@orvilma.com
        </li>
        <li class="contact__item">
          <svg class="contact__icon" viewBox="0 0 8 8" aria-hidden="true"><circle cx="4" cy="4" r="4" fill="var(--brand-red)"/></svg>
          www.orvilma.com
        </li>
        <li class="contact__item">
          <svg class="contact__icon" viewBox="0 0 8 8" aria-hidden="true"><rect width="8" height="8" rx="1.5" fill="var(--brand-red)"/></svg>
          / @orvilmaAT
        </li>
      </ul>
    </div>
  </section>

  <section class="card card--back" aria-label="Card back">
    <span class="back-mark" aria-hidden="true"></span>
    <h1 class="wordmark">ORVILMA</h1>
    <div class="rule"></div>
    <p class="tagline">ARQUITECTURA TÉCNICA</p>
  </section>
</body>
</html>
```